Business Card Design Project For Moving Company

Hello,

We need the business card to be 2 sided and we were thinking to use the logo on the front of the card (see file 1 attached) and the text "logo" (see file 2 attached) in the back of the card. We're looking for a powerful design that will help us build our brand, as our company is new.
We are a full service moving company (no storage) located in San Diego, CA, USA. The design should communicate to our potential customers that we have the highest level of service, customer satisfaction is our number one goal, our team is professional and efficient.

Thank you,

Gil
Updates

Project Deadline Extended
Reason: We would like to have more time to provide feedback for the designs already submitted. Thank you, Gil

Industry/Entity Type

Moving Company

Requirements
Must have
• Front of the card must have the following text and logo:
Haul Brightway, Inc
Residential And Commercial
Local And Long Distance
Address: 3917 Alder Crest Rd, #412,
San Diego, CA, 92087
P: 855-372-LIFT (5438)
F: 858-291-4476
info@haul-brightway.com
www.haul-brightway.com

Back of the card must have the following text and text "logo" (file 2 attached):

The best compliment we can ever receive is a referral from our clients.

```html
<!DOCTYPE html>
<html lang="en">
<head>
<meta charset="utf-8">
<title>Haul Brightway, Inc – Business Card</title>
<link rel="stylesheet" href="https://fonts.googleapis.com/css2?family=Arimo:wght@400;700&family=Open+Sans:wght@400&display=swap">
<style>
  :root {
    --backdrop: #8d5f38;
    --label: #1c140d;
    --card-white: #ffffff;
    --brand-red: #e2231f;
    --brand-dark: #3b3b3d;
    --text-grey: #555558;
    --rule-grey: #c9c9c9;
    --swoosh-grey: #4a4a4c;
    --dark-card-top: #3c3c3e;
    --dark-card-mid: #5a5a5c;
    --dark-card-bottom: #1f1f20;
  }
  * { margin: 0; padding: 0; box-sizing: border-box; }
  html, body { width: 1200px; height: 788px; overflow: hidden; }
  body {
    position: relative;
    background: var(--backdrop);
    font-family: "Arimo", Arial, sans-serif;
  }
  .side-label {
    position: absolute;
    width: 525px;
    text-align: center;
    font-family: "Open Sans", Arial, sans-serif;
    font-size: 21px;
    color: var(--label);
  }
  .card {
    position: absolute;
    width: 525px;
    height: 300px;
    border-radius: 22px;
    overflow: hidden;
    background: var(--card-white);
  }
  .card--front  { left: 57px;  top: 73px; }
  .card--back-1 { left: 622px; top: 73px; }
  .card--back-2 { left: 54px;  top: 445px; }
  .card--back-3 {
    left: 622px; top: 445px;
    background: linear-gradient(180deg, var(--dark-card-top) 0%, var(--dark-card-mid) 38%, var(--dark-card-bottom) 100%);
  }
  .swooshes { position: absolute; inset: 0; width: 525px; height: 300px; }
  .front-mark {
    position: absolute;
    left: 60px; top: 100px;
    width: 170px;
    text-align: center;
    font-weight: 700;
    font-size: 25px;
    line-height: 1.15;
    letter-spacing: 0.5px;
    color: var(--brand-red);
    text-transform: uppercase;
  }
  .front-divider {
    position: absolute;
    left: 238px; top: 66px;
    width: 1px; height: 180px;
    background: var(--rule-grey);
  }
  .contact {
    position: absolute;
    left: 281px; top: 70px;
    font-size: 14px;
    color: var(--text-grey);
    list-style: none;
    line-height: 18px;
  }
  .contact li { margin-bottom: 6px; }
  .contact .services { margin-bottom: 6px; }
  .contact em { font-style: italic; }
  .wordmark {
    position: absolute;
    left: 0; right: 0; top: 92px;
    text-align: center;
    font-weight: 700;
    font-size: 49px;
    letter-spacing: -0.5px;
    text-transform: uppercase;
    color: var(--brand-dark);
  }
  .card--back-3 .wordmark { color: var(--card-white); }
  .web-address {
    position: absolute;
    left: 0; right: 0; top: 256px;
    text-align: center;
    font-size: 17px;
    letter-spacing: 2.6px;
    color: var(--brand-dark);
  }
  .card--back-3 .web-address { color: var(--card-white); }
</style>
</head>
<body>

  <div class="side-label" style="left:57px; top:33px;">Front</div>
  <div class="side-label" style="left:622px; top:33px;">Back - 1</div>
  <div class="side-label" style="left:54px; top:404px;">Back - 2</div>
  <div class="side-label" style="left:622px; top:404px;">Back - 3</div>

  <section class="card card--front" aria-label="Card front">
    <svg class="swooshes" viewBox="0 0 525 300" aria-hidden="true">
      <path d="M352,0 Q468,6 525,58 L525,44 Q476,6 418,0 Z" fill="var(--swoosh-grey)"/>
      <path d="M410,0 Q492,12 525,76 L525,46 Q500,12 462,0 Z" fill="var(--brand-red)"/>
      <path d="M0,246 Q46,290 150,300 L92,300 Q30,288 0,262 Z" fill="var(--swoosh-grey)"/>
      <path d="M0,262 Q34,292 110,300 L60,300 Q16,290 0,280 Z" fill="var(--brand-red)"/>
    </svg>

    <div class="front-mark">Haul<br>Brightway</div>
    <div class="front-divider"></div>

    <ul class="contact">
      <li class="services">Residential And Commercial<br>Local And Long Distance</li>
      <li><em>p</em> : 855-372-LIFT (5438)</li>
      <li><em>f</em> : 858-291-4476</li>
      <li><em>e</em> : info@haul-brightway.com</li>
      <li><em>w</em> : www.haul-brightway.com</li>
      <li>3917 Alder Crest Rd, #412<br>San Diego, CA, 92087</li>
    </ul>
  </section>

  <section class="card card--back-1" aria-label="Card back, option 1">
    <div class="wordmark">Haul Brightway</div>
    <div class="web-address">www.haul-brightway.com</div>
  </section>

  <section class="card card--back-2" aria-label="Card back, option 2">
    <div class="wordmark">Haul Brightway</div>
    <div class="web-address">www.haul-brightway.com</div>
  </section>

  <section class="card card--back-3" aria-label="Card back, option 3">
    <div class="wordmark">Haul Brightway</div>
    <div class="web-address">www.haul-brightway.com</div>
  </section>

</body>
</html>
```